Jolly Paws Business Card Update

I have a business card which I love. I want to keep the same logo, colours, font and style. I want to upgrade the scripting and remove some elements and add others.
On the front side under Services - remove the existing wording and insert - Providing individual coaching strategies to create happy, healthy and social canine companions
Under Rebecca Thornbury amend the current wording to read: Qualified in Dog Behavioural Training, Natural Animal Healthcare and Animal Health Science
On the reverse side to remove the web address.

```html
<!DOCTYPE html>
<html lang="en">
<head>
<meta charset="utf-8">
<title>Jolly Paws Business Card</title>
<link href="https://fonts.googleapis.com/css2?family=Arimo:wght@400;700&display=swap" rel="stylesheet">
<style>
  :root {
    --stage: #2b2b2d;
    --blue-light: #0aa0dc;
    --blue-deep: #1f48a6;
    --red-bright: #ee2027;
    --red-deep: #6e0b10;
    --cream: #f3ecd0;
    --white: #ffffff;
    --ink: #2a2a2a;
    --rule: rgba(255,255,255,0.55);
  }
  * { box-sizing: border-box; margin: 0; padding: 0; }
  html, body {
    width: 1200px; height: 866px; overflow: hidden;
    background: var(--stage);
    font-family: "Arimo", Arial, sans-serif;
  }
  .sheet {
    position: relative; width: 1200px; height: 866px;
    display: flex; flex-direction: column; align-items: center; justify-content: center; gap: 40px;
  }
  .card {
    position: relative; width: 640px; height: 366px; overflow: hidden;
    box-shadow: 0 12px 30px rgba(0,0,0,0.55);
  }
  .blue-field {
    position: absolute; left: 0; top: 0; right: 0;
    background: linear-gradient(200deg, var(--blue-light) 0%, var(--blue-deep) 100%);
  }
  .red-field {
    position: absolute; left: 0; right: 0; bottom: 0;
    background: linear-gradient(100deg, var(--red-deep) 0%, var(--red-bright) 35%, var(--red-bright) 50%, var(--red-deep) 100%);
  }

  /* Front */
  .card-front .blue-field { height: 292px; border-bottom: 4px solid var(--white); }
  .card-front .red-field { height: 74px; }
  .brand-disc {
    position: absolute; left: 380px; top: 40px; width: 150px; height: 150px; border-radius: 50%;
    background: radial-gradient(circle, var(--cream) 55%, #d9c98e 100%);
    border: 9px solid var(--red-bright);
  }
  .brand-name {
    position: absolute; left: 60px; top: 200px; width: 520px; text-align: center;
    font-size: 52px; font-weight: 700; letter-spacing: 3px; color: var(--cream);
    text-transform: uppercase;
  }
  .tagline {
    position: absolute; left: 0; right: 0; bottom: 24px; text-align: center;
    color: var(--white); font-size: 19px; letter-spacing: 1px; text-transform: uppercase;
  }

  /* Back */
  .card-back .blue-field { height: 170px; }
  .mission-band {
    position: absolute; left: 0; right: 0; top: 170px; height: 26px;
    background: var(--white); color: var(--ink);
    font-size: 14.5px; line-height: 26px; text-align: center;
  }
  .card-back .red-field { height: 170px; }
  .back-disc {
    position: absolute; left: 100px; top: 28px; width: 120px; height: 120px; border-radius: 50%;
    background: radial-gradient(circle, var(--cream) 55%, #d9c98e 100%);
    border: 7px solid var(--red-bright);
  }
  .divider { position: absolute; left: 258px; top: 30px; width: 1px; height: 118px; background: var(--rule); }
  .services { position: absolute; left: 282px; top: 40px; width: 330px; color: var(--white); }
  .services h2 { font-weight: 400; font-size: 20px; letter-spacing: 1.5px; margin-bottom: 8px; }
  .services p { font-size: 15px; line-height: 1.3; }
  .contact { position: absolute; left: 0; right: 0; bottom: 0; height: 170px; color: var(--white); text-align: center; }
  .qualification { font-size: 14.5px; line-height: 1.35; margin-top: 18px; padding: 0 40px; }
  .person-name { font-size: 28px; margin-top: 12px; letter-spacing: 0.5px; }
  .contact-row {
    display: flex; justify-content: space-between; padding: 0 46px; margin-top: 22px; font-size: 16px;
  }
  .contact-item { display: flex; align-items: center; gap: 7px; }
  .contact-item svg { width: 18px; height: 18px; }
</style>
</head>
<body>
<main class="sheet">
  <section class="card card-front" aria-label="Business card front">
    <div class="blue-field"></div>
    <div class="red-field"></div>
    <div class="brand-disc"></div>
    <div class="brand-name">Jolly Paws</div>
    <div class="tagline">Happy Dogs, Happy Owners</div>
  </section>

  <section class="card card-back" aria-label="Business card reverse">
    <div class="blue-field"></div>
    <div class="back-disc"></div>
    <div class="divider"></div>
    <div class="services">
      <h2>SERVICES</h2>
      <p>Providing individual coaching strategies to create happy, healthy and social canine companions</p>
    </div>
    <div class="mission-band">Promoting communication and connection between dogs and their families</div>
    <div class="red-field"></div>
    <div class="contact">
      <p class="qualification">Qualified in Dog Behavioural Training, Natural Animal Healthcare and Animal Health Science</p>
      <p class="person-name">Rebecca Thornbury</p>
      <div class="contact-row">
        <span class="contact-item">
          <svg viewBox="0 0 20 20" aria-hidden="true"><circle cx="10" cy="10" r="9" fill="#fff"/><rect x="7" y="4.5" width="6" height="11" rx="1" fill="none" stroke="#b3141b" stroke-width="1.6"/></svg>
          0412 487 209
        </span>
        <span class="contact-item">
          <svg viewBox="0 0 20 20" aria-hidden="true"><circle cx="10" cy="10" r="9" fill="#fff"/><rect x="5" y="6.5" width="10" height="7" fill="none" stroke="#b3141b" stroke-width="1.5"/><path d="M5 6.5 L10 11 L15 6.5" fill="none" stroke="#b3141b" stroke-width="1.5"/></svg>
          hello@jollypawscoaching.com
        </span>
      </div>
    </div>
  </section>
</main>
</body>
</html>
```